Legal Service Estimated Retainer and Average Case Value

We need an 11x14 flyer that contains the standard retainers and average cost be case, both provided in documents, for each case type we handle. We need the information displayed, preferably in a way that makes the information readable but less troubling to a client shocked at price of litigation. We need one sheet with the retainers and average case value merged into one table.

Target Market(s)

Potential Clients

Font styles to use
Serif
Sans Serif

```html
<!DOCTYPE html>
<html lang="en">
<head>
<meta charset="utf-8">
<title>Average Fee Per Case Type</title>
<link href="https://fonts.googleapis.com/css2?family=Montserrat:wght@400;500;600;700&display=swap" rel="stylesheet">
<style>
  :root {
    --navy: #0d1b52;
    --ink: #27316b;
    --paper: #e9e9eb;
    --strip: #d7d7da;
    --white: #ffffff;
    --backdrop: #4a4a4a;
  }
  * { box-sizing: border-box; margin: 0; padding: 0; }
  html, body { width: 1200px; height: 800px; overflow: hidden; }
  body {
    background: radial-gradient(circle at 50% 45%, #6a6a6a 0%, var(--backdrop) 70%, #3a3a3a 100%);
    font-family: "Montserrat", Arial, sans-serif;
    color: var(--ink);
    position: relative;
  }
  .flyer {
    position: absolute;
    left: 330px; top: 20px;
    width: 540px; height: 760px;
    background: var(--paper);
    box-shadow: 0 10px 30px rgba(0,0,0,.45);
    display: flex; flex-direction: column;
  }
  .masthead {
    height: 66px; background: var(--white);
    display: flex; align-items: center; gap: 10px;
    padding-left: 14px;
  }
  .masthead-mark { width: 30px; height: 30px; background: var(--navy); }
  .masthead-name {
    font-weight: 600; font-size: 13px; letter-spacing: .6px;
    color: var(--navy); text-transform: uppercase;
  }
  .section-band {
    background: var(--navy); color: var(--white);
    height: 26px; line-height: 26px; text-align: center;
    font-weight: 700; font-size: 15px; letter-spacing: .3px;
  }
  .intro {
    font-size: 7.6px; line-height: 15px; text-transform: uppercase;
    padding: 8px 14px 6px 22px; text-indent: 50px; color: #2b2f45;
  }
  .fee-table { padding: 0 0 6px; }
  .table-head {
    display: flex; justify-content: space-between; align-items: center;
    background: var(--strip); height: 23px; padding: 0 20px 0 20px;
    font-weight: 700; font-size: 15px; color: var(--navy);
    margin-bottom: 6px;
  }
  .fee-row {
    display: flex; justify-content: space-between;
    height: 18px; line-height: 18px;
    padding: 0 40px 0 22px;
    font-size: 10.4px; letter-spacing: .4px; text-transform: uppercase;
  }
  .fee-row .amount { font-weight: 600; color: var(--navy); letter-spacing: .2px; }
  .footer-band { margin-top: auto; height: 22px; background: var(--navy); }
</style>
</head>
<body>
  <main class="flyer">
    <header class="masthead">
      <div class="masthead-mark"></div>
      <div class="masthead-name">Law Office of Daniel R Whitmore</div>
    </header>

    <h1 class="section-band">AVERAGE FEE PER CASE TYPE</h1>
    <p class="intro">In order for our clients to set expectations for legal fees, we provide the national average range of fees per case type. These are only to provide you with an understanding of what other cases have cost clients in similar cases. Please note these are not estimates nor guarantees of your own legal costs.</p>

    <section class="fee-table">
      <div class="table-head"><span>CASE TYPE</span><span>FEE PER CASE</span></div>
      <div class="fee-row"><span>Custody Contempt/Modification</span><span class="amount">$5,000 - $8,000</span></div>
      <div class="fee-row"><span>Custody Initial Order</span><span class="amount">$4,000 - $7,000</span></div>
      <div class="fee-row"><span>Custody &amp; Support</span><span class="amount">$5,000 - $8,000</span></div>
      <div class="fee-row"><span>Support</span><span class="amount">$2,000 - $4,000</span></div>
      <div class="fee-row"><span>Divorce (3301C)</span><span class="amount">$1,500 - $3,000</span></div>
      <div class="fee-row"><span>Divorce (3301D)</span><span class="amount">$2,000 - $3,000</span></div>
      <div class="fee-row"><span>Protection From Abuse</span><span class="amount">$1,500 - $3,000</span></div>
      <div class="fee-row"><span>Divorce &amp; Custody</span><span class="amount">$5,000 - $8,000</span></div>
      <div class="fee-row"><span>Divorce &amp; Equitable Distribution</span><span class="amount">$6,000 - $10,000</span></div>
      <div class="fee-row"><span>Divorce, Custody &amp; Support</span><span class="amount">$8,000 - $12,000</span></div>
      <div class="fee-row"><span>Divorce, Equitable Distribution &amp; Custody</span><span class="amount">$10,000 - $15,000</span></div>
      <div class="fee-row"><span>Divorce, Equitable Distribution &amp; Support</span><span class="amount">$8,000 - $12,000</span></div>
      <div class="fee-row"><span>Divorce, Equitable Distribution, Custody &amp; Support</span><span class="amount">$12,000 - $15,000</span></div>
    </section>

    <h2 class="section-band">RETAINERS AND TOTAL ESTIMATED CASE COSTS</h2>

    <section class="fee-table">
      <div class="table-head"><span>CASE TYPE</span><span>FEE PER CASE</span></div>
      <div class="fee-row"><span>Divorce (3301 C)</span><span class="amount">RETAINER: $2,000</span></div>
      <div class="fee-row"><span>Divorce (3301 D)</span><span class="amount">RETAINER: $2,500</span></div>
      <div class="fee-row"><span>Divorce and Custody</span><span class="amount">RETAINER: $3,500</span></div>
      <div class="fee-row"><span>Divorce and Equitable Distribution</span><span class="amount">RETAINER: $3,500</span></div>
      <div class="fee-row"><span>Divorce and Support</span><span class="amount">RETAINER: $3,500</span></div>
      <div class="fee-row"><span>Divorce, Custody and Support</span><span class="amount">RETAINER: $4,000</span></div>
      <div class="fee-row"><span>Divorce, Equitable Distribution and Support</span><span class="amount">RETAINER: $4,000</span></div>
      <div class="fee-row"><span>Divorce, Equitable Distribution and Custody</span><span class="amount">RETAINER: $4,500</span></div>
      <div class="fee-row"><span>Divorce, Equitable Distribution, Custody and Support</span><span class="amount">RETAINER: $5,000</span></div>
      <div class="fee-row"><span>Custody Initial Order</span><span class="amount">RETAINER: $3,000</span></div>
      <div class="fee-row"><span>Custody Modification</span><span class="amount">RETAINER: $3,000</span></div>
      <div class="fee-row"><span>Custody and Support</span><span class="amount">RETAINER: $3,500</span></div>
      <div class="fee-row"><span>(PFA) Protection From Abuse</span><span class="amount">RETAINER: $1,500</span></div>
    </section>

    <footer class="footer-band"></footer>
  </main>
</body>
</html>
```